Business Card - Rebranding for Consulting Firm

We are renaming and rebranding our consulting firm and need to raise the level of quality of our cards as part of that effort. We consult to leading high tech, life science and other innovation sector companies.

Need a two-sided business card design.

Side 1: (a) Company logo (b) tag line: Make Every Hire Count for More (c) Name (d) Title (e) Phone 1: Office (f) Phone 2: Mobile (g) email: person@HollowmereAdvisory.com

Side 2: Two lines of text: (a) Markets Shift. Teams Evolve. People Carry the Plan Forward Daily. (b) We help you lead through it all.

Target Market(s)

Business and human resources executives and senior managers

Industry/Entity Type

Management Consulting

Contact Information for Business Card

Font styles to use
Sans Serif

Requirements
Must have
• clean, not too busy, but with a bit of creativity. Stick to the colors used in the attached logo
• appeal to high tech, life science companies
Nice to have
• prefer white background

```html
<!DOCTYPE html>
<html lang="en">
<head>
<meta charset="utf-8">
<title>Hollowmere Advisory – Business Card</title>
<link href="https://fonts.googleapis.com/css2?family=Source+Sans+3:ital,wght@0,400;0,600;1,400;1,600&display=swap" rel="stylesheet">
<style>
  :root {
    --page-bg: #ecebe8;
    --brand-blue: #0068a3;
    --stripe-light: #1aa6e0;
    --stripe-mid: #0f8cc7;
    --stripe-dark: #0a73b3;
    --panel-grey: #6f8593;
    --white: #ffffff;
    --logo-blue: #0a6fae;
  }
  * { margin: 0; padding: 0; box-sizing: border-box; }
  html, body {
    width: 1200px; height: 987px; overflow: hidden;
    background: var(--page-bg);
    font-family: "Source Sans 3", sans-serif;
  }
  .canvas { position: relative; width: 1200px; height: 987px; }

  .card {
    position: absolute; left: 293px; width: 615px; height: 352px;
    box-shadow: 0 2px 6px rgba(0,0,0,0.18);
  }
  .card--front { top: 130px; background: var(--white); display: flex; }
  .card--back { top: 506px; background: var(--brand-blue); color: var(--white); }

  /* front */
  .edge-stripe { width: 13px; height: 100%; display: flex; flex-direction: column; }
  .edge-stripe span { flex: 1; }
  .edge-stripe span + span { border-top: 2px solid var(--white); }
  .edge-stripe .s1 { background: var(--stripe-light); }
  .edge-stripe .s2 { background: var(--stripe-mid); }
  .edge-stripe .s3 { background: var(--stripe-dark); }

  .brand-area {
    width: 276px; height: 100%;
    display: flex; align-items: center; justify-content: center;
  }
  .wordmark {
    display: flex; align-items: center; gap: 8px;
    color: var(--logo-blue); font-weight: 600; font-size: 25px; letter-spacing: -0.3px;
  }
  .wordmark__square { width: 14px; height: 14px; background: var(--logo-blue); }

  .contact-panel {
    flex: 1; height: 100%; background: var(--panel-grey); color: var(--white);
    padding: 78px 0 0 21px;
  }
  .person-name { font-size: 24px; font-weight: 600; line-height: 1.1; }
  .person-title { font-size: 16.5px; line-height: 1.2; margin-top: 1px; }
  .contact-list { list-style: none; margin-top: 10px; }
  .contact-list li {
    display: flex; align-items: center; gap: 8px;
    font-size: 16px; line-height: 23.5px;
  }
  .contact-list svg { width: 14px; height: 14px; flex: none; fill: var(--white); }
  .tagline { margin-top: 17px; font-size: 16.5px; font-weight: 600; font-style: italic; }

  /* back */
  .back-wordmark {
    position: absolute; top: 142px; left: 0; right: 0;
    display: flex; justify-content: center; align-items: center; gap: 12px;
    font-weight: 600; font-size: 40px; letter-spacing: -0.5px;
  }
  .back-wordmark .wordmark__square { width: 20px; height: 20px; background: var(--white); }
  .manifesto {
    position: absolute; top: 268px; left: 0; right: 0;
    text-align: center; font-style: italic; font-size: 17px;
  }
  .manifesto__rule {
    width: 470px; height: 1px; margin: 7px auto 8px;
    background: linear-gradient(90deg, rgba(255,255,255,0), rgba(255,255,255,0.7), rgba(255,255,255,0));
  }
</style>
</head>
<body>
<div class="canvas">

  <section class="card card--front">
    <div class="edge-stripe"><span class="s1"></span><span class="s2"></span><span class="s3"></span></div>
    <div class="brand-area">
      <div class="wordmark"><span class="wordmark__square"></span>Hollowmere Advisory</div>
    </div>
    <div class="contact-panel">
      <h1 class="person-name">Daniel Rourke</h1>
      <p class="person-title">CEO/Founder</p>
      <ul class="contact-list">
        <li>
          <svg viewBox="0 0 24 24"><path d="M6.6 10.8a15.1 15.1 0 0 0 6.6 6.6l2.2-2.2c.3-.3.7-.4 1-.2 1.1.4 2.3.6 3.6.6.6 0 1 .4 1 1V20c0 .6-.4 1-1 1A17 17 0 0 1 3 4c0-.6.4-1 1-1h3.5c.6 0 1 .4 1 1 0 1.3.2 2.5.6 3.6.1.3 0 .7-.2 1z"/></svg>
          555 214 0917
        </li>
        <li>
          <svg viewBox="0 0 24 24"><path d="M7 1h10a2 2 0 0 1 2 2v18a2 2 0 0 1-2 2H7a2 2 0 0 1-2-2V3a2 2 0 0 1 2-2zm0 3v14h10V4zm5 15.5a1 1 0 1 0 0 2 1 1 0 0 0 0-2z"/></svg>
          555 380 6142
        </li>
        <li>
          <svg viewBox="0 0 24 24"><path d="M2 5h20v14H2zm2 2v.5l8 5 8-5V7zm0 2.8V17h16V9.8l-8 5z"/></svg>
          person@HollowmereAdvisory.com
        </li>
        <li>
          <svg viewBox="0 0 24 24"><path d="M12 2a10 10 0 1 0 0 20 10 10 0 0 0 0-20zm-1 17.9A8 8 0 0 1 4.2 10L9 14.8v1a2 2 0 0 0 2 2zm6.9-2.5A2 2 0 0 0 16 16h-1v-3a1 1 0 0 0-1-1H8v-2h2a1 1 0 0 0 1-1V7h2a2 2 0 0 0 2-2v-.4a8 8 0 0 1 2.9 12.8z"/></svg>
          www.HollowmereAdvisory.com
        </li>
      </ul>
      <p class="tagline">Make Every Hire Count for More</p>
    </div>
  </section>

  <section class="card card--back">
    <div class="back-wordmark"><span class="wordmark__square"></span>Hollowmere Advisory</div>
    <div class="manifesto">
      <p>Markets Shift. Teams Evolve. People Carry the Plan Forward Daily.</p>
      <div class="manifesto__rule"></div>
      <p>We help you lead through it all.</p>
    </div>
  </section>

</div>
</body>
</html>
```